Lawn & Garden Maintenace Business card design needed

I need a basic business card design for a Lawn Mowing & Garden Maintenance business

I would like it to look a combination of classy, striking, with vibrant Green/s, I will attached a very rough idea of what I would like but I am open to new suggestions, and the possibility of doing it on a darker charcoal or black gloss card, please don't just send me a version of what I've attached it's a very rough idea & more based around the text layout than anything else, feel free to let your creative instincts fly!

Must have grass across the bottom of the Card & i would prefer it to be portrait rather than landscape.

I quite like the coloring of this previously submitted card
http://www.pixelbrief.com/design/4829163

Please have the text in White and Green if you are submitting a dark card, thank you.

K.R. Lawn & Garden Services

Free Quote - Great Rates

Kel Ropani
0417 362 918
Info@KRLawnAndGarden.com.au

Must have
• Must have grass across bottom of card preferably photo real grass rather than illustrated.
Nice to have
• Small telephone icon for phone number small email icon for email address but only if both icon are similar size and don't take away from the overall look of the card

Would also be nice to a have a flow/style that would be easily transferable to flyers & advertising

```html
<!DOCTYPE html>
<html lang="en">
<head>
<meta charset="utf-8">
<title>K.R. Lawn &amp; Garden Services – Business Card</title>
<link rel="stylesheet" href="https://fonts.googleapis.com/css2?family=Archivo:wght@800&display=swap">
<style>
  :root {
    --stage: #2b2b2b;
    --card-black: #050505;
    --grass-shadow: #14300b;
    --grass-deep: #24601a;
    --grass-mid: #3f8f22;
    --grass-bright: #62b52e;
    --white: #ffffff;
    --gloss: rgba(255, 255, 255, 0.06);
  }
  * { margin: 0; padding: 0; box-sizing: border-box; }
  html, body {
    width: 1200px;
    height: 900px;
    overflow: hidden;
    background: var(--stage);
  }
  .canvas {
    position: relative;
    width: 1200px;
    height: 900px;
    display: flex;
    align-items: center;
    justify-content: center;
  }
  .business-card {
    position: relative;
    width: 1000px;
    height: 570px;
    background: var(--card-black);
    overflow: hidden;
    border-radius: 4px;
    box-shadow: 0 20px 50px rgba(0, 0, 0, 0.55);
    font-family: "Archivo", Arial, sans-serif;
    font-weight: 800;
    color: var(--white);
  }
  .grass-photo {
    position: absolute;
    left: 0; right: 0; bottom: 0;
    height: 58%;
    background: linear-gradient(to bottom,
      rgba(5, 5, 5, 0) 0%,
      var(--grass-shadow) 22%,
      var(--grass-deep) 45%,
      var(--grass-mid) 72%,
      var(--grass-bright) 100%);
  }
  .gloss-sheen {
    position: absolute;
    inset: 0;
    pointer-events: none;
  }
  .wordmark {
    position: absolute;
    left: 70px;
    top: 215px;
    display: flex;
    align-items: center;
    gap: 22px;
  }
  .wordmark-dot {
    width: 40px;
    height: 40px;
    border-radius: 50%;
    background: var(--white);
    flex: none;
  }
  .wordmark-name {
    font-size: 46px;
    font-weight: 800;
    line-height: 1.08;
    text-transform: uppercase;
    letter-spacing: 0.5px;
  }
  .wordmark-name span { display: block; }
  .offer {
    position: absolute;
    left: 560px;
    top: 110px;
    font-size: 34px;
    letter-spacing: 1px;
    text-transform: uppercase;
    line-height: 1;
  }
  .offer-divider {
    margin: 14px 0 14px 10px;
    width: 360px;
    border-top: 3px dashed var(--white);
  }
  .offer-rates { padding-left: 20px; }
  .contact {
    position: absolute;
    left: 620px;
    top: 305px;
    text-transform: uppercase;
  }
  .contact-name {
    display: flex;
    align-items: center;
    font-size: 28px;
    letter-spacing: 1px;
  }
  .contact-name .trail {
    width: 150px;
    margin-left: 20px;
    border-top: 3px dashed var(--white);
  }
  .contact-phone {
    font-size: 22px;
    margin-top: 8px;
    padding-left: 30px;
    letter-spacing: 1px;
  }
  .contact-email {
    position: absolute;
    left: 330px;
    top: 425px;
    font-size: 24px;
    letter-spacing: 1px;
    text-transform: uppercase;
  }
</style>
</head>
<body>
<main class="canvas">
  <section class="business-card" aria-label="K.R. Lawn and Garden Services business card">
    <div class="grass-photo" role="img" aria-label="Photo of lush green lawn grass across the bottom of the card"></div>
    <svg class="gloss-sheen" width="1000" height="570" viewBox="0 0 1000 570" aria-hidden="true">
      <path d="M520 0 L1000 0 L1000 40 Q760 120 600 570 L470 570 Q560 220 520 0 Z" fill="var(--gloss)"/>
    </svg>

    <div class="wordmark">
      <span class="wordmark-dot" aria-hidden="true"></span>
      <h1 class="wordmark-name"><span>K.R. Lawn &amp;</span><span>Garden Services</span></h1>
    </div>

    <div class="offer">
      <div class="offer-quote">Free Quote</div>
      <div class="offer-divider"></div>
      <div class="offer-rates">Great Rates</div>
    </div>

    <div class="contact">
      <div class="contact-name">Kel Ropani<span class="trail"></span></div>
      <div class="contact-phone">Ph: 0417 362 918</div>
    </div>

    <div class="contact-email">Info@KRLawnAndGarden.com.au</div>
  </section>
</main>
</body>
</html>
```